Motion Nest Business Cards

Can all designers please apply the following info on their designs' back-side of the business card: (please see brief file upload ('Info for backside...' - for required info, colours & layout)

SPECIALISING IN INDIVIDUAL PILATES INSTRUCTION
MATWORK – including small apparatus
and STUDIO:
VIVANTE 3 GLIDER
LADDER BARREL
COUNTOUR BARREL
FLEXI DOME
VIM STOOL
KIM-O-LAN

Business Cards for Motion Nest - applying the Motion Nest logo design selected earlier.
Note the business card requires both a front and back side. Please refer to two uploaded ppt-files for type of info required to be displayed, and rough position of where info could be. Require innovative / fresh approach to business card design and use of colour by designers now. Please refer to and use logo as uploaded - also for potential business card colour application.

Dear Designers,

Please note the additional inclusion / upload of two draft ppt-files that try to show where I want what type of information, for both the front & back sides of the required business card, plus an attempt at showing the high-level concept / idea of business info position.

As my 'drafts' obviously lack colour and any ability towards innovative card design or approach – I now rely on your vastly superior graphic design abilities to produce a really great business card for my business…

Looking forward to your submissions!

Kind regards, Merika for: Motion Nest 

Hello all Designers,

Can all designers please apply the following info on their designs' back-side of the business card: (please see / refer to the Brief and specifically the file upload ('Info for backside...' - for required info, colours & layout) - for the backside of the business card).

Info content (without colour, layout etc.):

and STUDIO:

VIVANTE 3 GLIDER

LADDER BARREL

COUNTOUR BARREL

FLEXI DOME

VIM STOOL

KIM-O-LAN

Thank you to all designers that submitted for consideration!

With regards,

Motion Nest

```html
<!DOCTYPE html>
<html lang="en">
<head>
<meta charset="utf-8">
<title>Motion Nest – Business Cards</title>
<link rel="stylesheet" href="https://fonts.googleapis.com/css2?family=Cinzel:wght@400;700&family=Questrial&family=Cormorant+Garamond:ital,wght@1,600&display=swap">
<style>
  :root {
    --bg: #d9d9d9;
    --paper: #ffffff;
    --green: #4a7a1a;
    --orange: #e0531e;
    --text-light: #ffffff;
    --faint: rgba(224, 83, 30, 0.13);
  }
  * { margin: 0; padding: 0; box-sizing: border-box; }
  html, body { width: 1200px; height: 871px; overflow: hidden; background: var(--bg); }
  .canvas { position: relative; width: 1200px; height: 871px; }

  .card {
    position: absolute;
    width: 620px; height: 379px;
    background: var(--paper);
    box-shadow: 0 6px 18px rgba(0,0,0,0.25);
    overflow: hidden;
  }
  .card-back { left: 170px; top: 40px; }
  .card-front { left: 410px; top: 452px; }
  .card svg.card-shape { position: absolute; inset: 0; }

  /* Back side */
  .watermark {
    position: absolute; left: 60px; top: 118px;
    display: flex; align-items: center; gap: 14px;
    font-family: "Questrial", sans-serif; font-size: 72px;
    color: var(--faint); white-space: nowrap;
  }
  .watermark .dot { width: 58px; height: 58px; border-radius: 50%; background: rgba(74,122,26,0.12); }
  .services {
    position: absolute; left: 0; right: 0; top: 34px;
    text-align: center; font-family: "Cinzel", serif; font-weight: 700;
    color: var(--green); font-size: 12px; letter-spacing: 0.5px;
  }
  .services .headline { color: var(--orange); font-size: 12.5px; margin-bottom: 10px; }
  .services .intro { margin-bottom: 8px; }
  .services ul { list-style: none; width: 210px; margin: 4px auto 0; }
  .services li { padding: 5px 0; border-bottom: 1px solid rgba(224,83,30,0.45); }
  .services li:last-child { border-bottom: none; }

  /* Front side */
  .brand {
    position: absolute; left: 34px; top: 30px;
    display: flex; align-items: center; gap: 14px;
  }
  .brand .dot { width: 46px; height: 46px; border-radius: 50%; background: var(--green); }
  .brand .name { font-family: "Questrial", sans-serif; font-size: 50px; color: var(--orange); line-height: 1; }
  .tagline {
    position: absolute; left: 118px; top: 94px;
    font-family: "Cormorant Garamond", serif; font-style: italic; font-weight: 600;
    font-size: 12px; letter-spacing: 2px; color: var(--green); text-transform: uppercase;
  }
  .tagline .sep { color: var(--orange); margin: 0 8px; }

  .person { position: absolute; left: 40px; top: 196px; white-space: nowrap; }
  .person .full-name { font-family: "Cinzel", serif; font-weight: 700; font-size: 18px; color: var(--text-light); letter-spacing: 1px; }
  .person .role { font-family: "Cinzel", serif; font-weight: 700; font-size: 10.5px; color: var(--orange); letter-spacing: 0.4px; margin-top: 2px; }

  .studio { position: absolute; left: 40px; top: 258px; font-family: "Questrial", sans-serif; color: var(--text-light); font-size: 12px; letter-spacing: 1px; line-height: 1.7; text-transform: uppercase; }
  .studio .label { font-family: "Cinzel", serif; font-weight: 700; }

  .contacts { position: absolute; left: 292px; top: 264px; list-style: none; font-family: "Questrial", sans-serif; color: var(--text-light); font-size: 12.5px; letter-spacing: 1px; }
  .contacts li { display: flex; align-items: center; gap: 12px; height: 25px; }
  .contacts svg { width: 14px; height: 14px; fill: none; stroke: var(--orange); stroke-width: 1.8; }
  .contacts .no-icon { width: 14px; }
</style>
</head>
<body>
<main class="canvas">

  <section class="card card-back" aria-label="Business card back">
    <svg class="card-shape" viewBox="0 0 620 379" width="620" height="379" aria-hidden="true">
      <path d="M0,318 C200,330 420,300 620,228 L620,379 L0,379Z" fill="var(--orange)"/>
      <path d="M0,334 C200,342 420,312 620,244 L620,379 L0,379Z" fill="var(--green)"/>
    </svg>
    <div class="watermark" aria-hidden="true"><span class="dot"></span>Motion Nest</div>
    <div class="services">
      <p class="headline">SPECIALISING IN INDIVIDUAL PILATES INSTRUCTION</p>
      <p class="intro">MATWORK – INCLUDING SMALL APPARATUS</p>
      <p>AND STUDIO:</p>
      <ul>
        <li>VIVANTE 3 GLIDER</li>
        <li>LADDER BARREL</li>
        <li>COUNTOUR BARREL</li>
        <li>FLEXI DOME</li>
        <li>VIM STOOL</li>
        <li>KIM-O-LAN</li>
      </ul>
    </div>
  </section>

  <section class="card card-front" aria-label="Business card front">
    <svg class="card-shape" viewBox="0 0 620 379" width="620" height="379" aria-hidden="true">
      <path d="M0,138 C200,148 380,188 620,238 L620,379 L0,379Z" fill="var(--orange)"/>
      <path d="M0,154 C200,164 380,204 620,254 L620,379 L0,379Z" fill="var(--green)"/>
    </svg>
    <div class="brand"><span class="dot"></span><span class="name">Motion Nest</span></div>
    <p class="tagline">Balance<span class="sep">•</span>Strength<span class="sep">•</span>Flexibility</p>

    <div class="person">
      <p class="full-name">MERIKA THORNQUIST</p>
      <p class="role">DIPLOMA OF PROFESSIONAL PILATES INSTRUCTION</p>
    </div>

    <div class="studio">
      <p class="label">Studio Location:</p>
      <p>18 Kestrel Lane</p>
      <p>Northbay WA 6190</p>
    </div>

    <ul class="contacts">
      <li><svg viewBox="0 0 16 16"><path d="M3 2h3l1.5 4-2 1.2a8 8 0 0 0 3.3 3.3L10 8.5l4 1.5v3a1.5 1.5 0 0 1-1.6 1.5A12 12 0 0 1 1.5 3.6 1.5 1.5 0 0 1 3 2z"/></svg>041 000 7391</li>
      <li><svg viewBox="0 0 16 16"><rect x="1.5" y="3.5" width="13" height="9" rx="1"/><path d="M1.5 4l6.5 5 6.5-5"/></svg>INFO@MOTIONNEST.COM</li>
      <li><svg viewBox="0 0 16 16"><circle cx="8" cy="8" r="6.5"/><path d="M1.5 8h13M8 1.5c2 2 2 11 0 13M8 1.5c-2 2-2 11 0 13"/></svg>WWW.MOTIONNEST.COM</li>
      <li><span class="no-icon"></span>WWW.MOTIONNEST.COM.AU</li>
    </ul>
  </section>

</main>
</body>
</html>
```